South African ISP needs Banner Ads designed

We require world-class Banner Ad design to showcase our new Capped Unshaped ADSL / Fibre product.

We need a modern, slick design that will deliver a High conversion rate.

Banners must include our Logo.

Text:

Capped Unshaped ADSL from R1 per GB!

```html
<!DOCTYPE html>
<html lang="en">
<head>
<meta charset="utf-8">
<title>netmara – Capped Unshaped ADSL banner</title>
<link rel="stylesheet" href="https://fonts.googleapis.com/css2?family=Lato:wght@400;700&display=swap">
<style>
  :root {
    --cream: #fbf7f0;
    --navy: #1d3a5c;
    --brand-blue: #2f6aa6;
    --teal-dark: #08303a;
    --teal-mid: #0f5a66;
    --teal-glow: #7fe3e6;
    --cable-green: #3fcf5c;
  }
  html, body {
    margin: 0;
    padding: 0;
    overflow: hidden;
    background: #ffffff;
  }
  .banner {
    position: relative;
    width: 1200px;
    height: 427px;
    overflow: hidden;
    background: var(--cream);
    font-family: "Lato", Arial, sans-serif;
  }
  .hero-visual {
    position: absolute;
    top: 0;
    right: 0;
    width: 700px;
    height: 100%;
    background:
      radial-gradient(ellipse 160px 90px at 560px 170px, rgba(63, 207, 92, 0.55), transparent 70%),
      radial-gradient(ellipse 260px 120px at 560px 110px, rgba(63, 207, 92, 0.25), transparent 75%),
      radial-gradient(ellipse 220px 260px at 160px 150px, rgba(127, 227, 230, 0.55), transparent 70%),
      linear-gradient(180deg, var(--teal-dark) 0%, #0b3f4a 55%, var(--teal-mid) 100%);
  }
  .hero-fade {
    position: absolute;
    top: 0;
    left: 440px;
    width: 360px;
    height: 100%;
    background: linear-gradient(90deg, var(--cream) 0%, rgba(251, 247, 240, 0.85) 35%, rgba(255, 255, 255, 0.35) 70%, rgba(255, 255, 255, 0) 100%);
  }
  .brand {
    position: absolute;
    top: 46px;
    left: 40px;
    display: flex;
    align-items: center;
    gap: 12px;
    color: var(--brand-blue);
    font-weight: 700;
    font-size: 38px;
    letter-spacing: 0.5px;
  }
  .brand-dot {
    width: 40px;
    height: 40px;
    border-radius: 50%;
    background: var(--brand-blue);
  }
  .headline {
    position: absolute;
    top: 170px;
    left: 37px;
    margin: 0;
    color: var(--navy);
    font-weight: 400;
    font-size: 45px;
    line-height: 62px;
    letter-spacing: 1.5px;
  }
</style>
</head>
<body>
  <div class="banner">
    <div class="hero-visual" role="img" aria-label="Glowing fibre optic strands and a green network cable with its connector on a dark teal background"></div>
    <div class="hero-fade"></div>
    <div class="brand">
      <span class="brand-dot"></span>
      <span class="brand-name">netmara</span>
    </div>
    <h1 class="headline">Capped Unshaped ADSL<br>from R1 per GB!</h1>
  </div>
</body>
</html>
```